Harbor Keyvault Password Manager WebApp Design

Harbor Keyvault is seeking an expert UI designer to provide a fresh and modern visual appeal for our product. Our inspiration comes from two major tools that have successfully managed to balance functionality and design aesthetics - Nimbus Folio and LockTrellis. We want our application to exude a similar trustworthiness and modernity, through a clean, intuitive and responsive design.
We have established preliminary mockups and would like the designer to work within these parameters while enhancing the overall user experience. The primary tasks will involve innovative and improved designs of the login screen and the password screen, both being crucial touchpoints for our users. The login screen also serves a crucial role in demonstrating how our system works.
Key Elements:
Logo Integration: We are providing the logo for Harbor Keyvault. The design should align with the logo, both in terms of colors and overall aesthetic, to ensure a cohesive brand identity.
Color Palette: The UI design should adhere to the color palette derived from the logo to maintain brand consistency. The design should effectively utilize these colors to highlight important elements and improve user engagement.
Trustworthy and Modern Design: The UI should be professional and trustworthy. It should mirror the look and feel of Nimbus Folio's simplicity and LockTrellis's solid security design, which inspires user confidence.
Adherence to Mockup Boundaries: The existing mockups serve as a guideline for the layout and placement of elements. The design should respect these boundaries while bringing innovation and visual appeal.
Improved Login Screen: The login screen is a key part of the user's journey and should be designed with utmost care. It should be intuitive, easy-to-use, visually engaging, and educative, showcasing how the system operates and encouraging users to sign in with confidence.
Enhanced Password Screen: The password screen, another key user touchpoint, needs improvement. The different types of passwords should be made more visible and intuitive, easing user interaction and enhancing the overall experience.
Prospective designers are encouraged to test our current version available for free at app.harborkeyvault.example to understand the product better and contribute to meaningful design enhancements.
The goal of this project is to provide a visually compelling and user-friendly interface for Harbor Keyvault that inspires user trust, while adhering to the branding elements, including color scheme and logo design. The ideal designer will have a proven track record of creating compelling UI designs that enhance user experience and engagement.
We preferred the design to be in Figma.
Please provide the 3 design so we can evaluate if we like to choice you:
1. Login Page.
2. Passwords View design
3. Single Passwod Page
We need all the pages to be design that are provided as screenshots.
Target Market(s)
Companies
Industry/Entity Type
Security,
Number of Pages Required
5+ page
Font styles to use
Look and feel
Each slider illustrates characteristics of the customer's brand and the style your logo design should communicate.

```html
<!DOCTYPE html>
<html lang="en">
<head>
<meta charset="utf-8">
<title>Harbor Keyvault – Login and Vault</title>
<link rel="stylesheet" href="https://fonts.googleapis.com/css2?family=Nunito+Sans:wght@300;400;600;700;800&family=Rubik:wght@500;600&display=swap">
<style>
  :root {
    --board: #e6e6e6;
    --panel: #f7f7f7;
    --white: #ffffff;
    --green: #21a660;
    --green-soft: #3bb273;
    --blue: #3d6fd6;
    --folder: #3f73d8;
    --ink: #1d1d1d;
    --muted: #555555;
    --line: #ececec;
    --avatar: #e8473b;
  }
  * { box-sizing: border-box; margin: 0; padding: 0; }
  html, body { width: 1035px; height: 1200px; overflow: hidden; }
  body {
    background: var(--board);
    font-family: "Nunito Sans", sans-serif;
    color: var(--ink);
    position: relative;
  }

  /* ---------- Login screen ---------- */
  .login {
    position: absolute; left: 53px; top: 44px; width: 928px; height: 526px;
    background: var(--panel);
    box-shadow: 0 1px 3px rgba(0,0,0,.08);
    text-align: center;
  }
  .brand {
    position: absolute; top: 78px; left: 0; right: 0;
    display: flex; justify-content: center; align-items: center; gap: 10px;
    font-size: 27px; font-weight: 400; color: #555;
  }
  .brand-mark { width: 26px; height: 26px; background: var(--green); border-radius: 4px; }
  .welcome {
    position: absolute; top: 112px; left: 0; right: 0;
    font-family: "Rubik", sans-serif; font-weight: 600; font-size: 19px; letter-spacing: .3px;
  }
  .intro {
    position: absolute; top: 143px; left: 0; right: 0;
    font-size: 13.5px; line-height: 20px; font-weight: 400;
  }
  .feature {
    position: absolute; top: 203px; width: 334px; height: 191px;
    background: var(--green); border-radius: 10px; overflow: hidden;
    color: var(--white);
  }
  .feature.keys { left: 117px; }
  .feature.storage { left: 478px; }
  .feature-badge {
    position: absolute; left: 112px; top: -28px; width: 110px; height: 110px;
    border-radius: 50%; background: var(--green-soft);
    display: flex; align-items: flex-end; justify-content: center; padding-bottom: 30px;
  }
  .feature-text {
    position: absolute; left: 16px; right: 16px;
    font-size: 13.5px; line-height: 20px; font-weight: 300;
  }
  .feature.keys .feature-text { top: 83px; }
  .feature.storage .feature-text { top: 98px; }
  .feature-text strong {
    display: block; margin-top: 7px;
    font-family: "Rubik", sans-serif; font-weight: 500; font-size: 13.5px;
  }
  .signin {
    position: absolute; left: 332px; top: 418px; width: 265px; height: 53px;
    border: 1px solid var(--blue); border-radius: 8px; background: var(--white);
    display: flex; align-items: center; padding: 0 14px 0 9px; text-align: left;
  }
  .avatar {
    width: 33px; height: 33px; border-radius: 50%; background: var(--avatar);
    color: var(--white); font-size: 17px; font-weight: 700;
    display: flex; align-items: center; justify-content: center; flex-shrink: 0;
  }
  .signin-text { margin-left: 10px; font-size: 10.5px; line-height: 17px; flex: 1; }
  .provider-dot { width: 24px; height: 24px; border-radius: 50%; border: 3px solid #b9b9b9; }
  .legal {
    position: absolute; top: 499px; left: 0; right: 0;
    font-size: 10px; color: var(--muted);
  }
  .legal b { color: var(--ink); font-weight: 600; }

  /* ---------- Vault screen ---------- */
  .vault {
    position: absolute; left: 53px; top: 616px; width: 928px; height: 526px;
    background: var(--panel);
    box-shadow: 0 1px 3px rgba(0,0,0,.08);
  }
  .rail {
    position: absolute; left: 0; top: 0; width: 58px; height: 100%;
    background: var(--green); color: var(--white);
  }
  .rail-item { position: absolute; left: 0; width: 58px; text-align: center; font-size: 10px; }
  .topbar {
    position: absolute; left: 58px; top: 0; right: 0; height: 45px; background: var(--white);
  }
  .section-title {
    position: absolute; top: 17px;
    font-family: "Rubik", sans-serif; font-weight: 500; font-size: 12.5px; color: var(--blue);
  }
  .search {
    position: absolute; right: 60px; top: 16px; font-size: 12px; color: #8a8a8a;
    display: flex; align-items: center; gap: 7px;
  }
  .categories {
    position: absolute; left: 66px; top: 49px; width: 178px; height: 464px;
    background: var(--white); border-radius: 10px; padding: 18px 0 0 14px;
    list-style: none;
  }
  .categories li {
    height: 22.5px; display: flex; align-items: center; gap: 7px;
    font-size: 10.5px; color: #333;
  }
  .cat-icon { width: 9px; text-align: center; font-size: 9px; color: #666; display: flex; justify-content: center; }
  .grid {
    position: absolute; left: 257px; top: 60px;
    display: grid; grid-template-columns: repeat(3, 214px); grid-auto-rows: 48px;
    column-gap: 5px; row-gap: 4.5px;
  }
  .entry {
    background: var(--white); border: 1px solid var(--line); border-radius: 5px;
    display: flex; align-items: center; gap: 10px; padding-left: 20px;
    font-size: 10.5px; color: #333;
  }
</style>
</head>
<body>

<section class="login" aria-label="Sign in screen">
  <div class="brand"><span class="brand-mark"></span>Harbor Keyvault</div>
  <h1 class="welcome">WELCOME</h1>
  <p class="intro">You can sign in or register from the button below.<br>Please keep in mind how our system works.</p>

  <article class="feature keys">
    <div class="feature-badge">
      <svg width="34" height="42" viewBox="0 0 34 42" fill="none" stroke="#fff" stroke-width="2.6">
        <path d="M9 18V11a8 8 0 0 1 16 0v2"/>
        <rect x="3" y="18" width="28" height="21" rx="2"/>
        <circle cx="17" cy="27" r="2.5" fill="#fff"/>
        <path d="M17 28v5"/>
      </svg>
    </div>
    <p class="feature-text">Your files are encrypted with different keys. They are dynamically aggregated only in your browser.
      <strong>We do not store your encryption/decryption keys.</strong></p>
  </article>

  <article class="feature storage">
    <div class="feature-badge">
      <svg width="32" height="42" viewBox="0 0 32 42" fill="none" stroke="#fff" stroke-width="2.6" stroke-linejoin="round">
        <path d="M3 3h18l8 8v28H3z"/>
        <path d="M21 3v8h8"/>
        <path d="M9 20h14M9 26h14M9 32h9"/>
      </svg>
    </div>
    <p class="feature-text">Your passwords are stored only on one place - your Nimbus Folio™.
      <strong>We do not store anything.</strong></p>
  </article>

  <div class="signin">
    <div class="avatar">O</div>
    <div class="signin-text">Sign in as Orchard<br>orchard.team@harborkeyvault.example</div>
    <div class="provider-dot"></div>
  </div>

  <p class="legal">By clicking ‘Continue with Nimbus”, you agree with our <b>Terms of Use</b> Learn what data we collect and how we handle it in our <b>Privacy Policy</b>.</p>
</section>

<section class="vault" aria-label="Vault screen">
  <nav class="rail">
    <div class="rail-item" style="top:16px">
      <svg width="16" height="15" viewBox="0 0 16 15" fill="#fff"><path d="M8 0 0 7h2v8h4v-5h4v5h4V7h2z"/></svg>
      <div>Vault</div>
    </div>
    <div class="rail-item" style="top:77px">
      <svg width="19" height="14" viewBox="0 0 19 14" fill="#fff"><circle cx="6" cy="4" r="3.5"/><circle cx="13.5" cy="4" r="3"/><path d="M0 14c0-4 3-6 6-6s6 2 6 6z"/><path d="M11 8.5c3-1.2 8 0 8 5.5h-6c0-2-.7-4-2-5.5z"/></svg>
    </div>
    <div class="rail-item" style="top:133px">
      <svg width="14" height="17" viewBox="0 0 14 17" fill="#fff"><path d="M7 0a1.5 1.5 0 0 1 1.5 1.6C11 2.3 12 4.5 12 7v4l2 2v1H0v-1l2-2V7c0-2.5 1-4.7 3.5-5.4A1.5 1.5 0 0 1 7 0z"/><path d="M5 15h4a2 2 0 0 1-4 0z"/></svg>
    </div>
    <div class="rail-item" style="top:193px">
      <svg width="15" height="12" viewBox="0 0 15 12" fill="#fff"><rect width="15" height="2.2"/><rect y="4.9" width="15" height="2.2"/><rect y="9.8" width="15" height="2.2"/></svg>
    </div>
  </nav>

  <header class="topbar">
    <h2 class="section-title" style="left:110px">CATEGORIES</h2>
    <h2 class="section-title" style="left:465px">LAST USED</h2>
    <div class="search">
      <svg width="11" height="11" viewBox="0 0 11 11" fill="none" stroke="#8a8a8a" stroke-width="1.4"><circle cx="4.5" cy="4.5" r="3.7"/><path d="M7.3 7.3 10.5 10.5"/></svg>
      Search
    </div>
  </header>

  <ul class="categories">
    <li><span class="cat-icon">▪</span>General</li>
    <li><span class="cat-icon">▪</span>Shared with me</li>
    <li><span class="cat-icon">▪</span>Work</li>
    <li><span class="cat-icon">▪</span>Social Media</li>
    <li><span class="cat-icon">▪</span>Shopping</li>
    <li><span class="cat-icon">✈</span>Travel</li>
    <li><span class="cat-icon">$</span>Banking</li>
    <li><span class="cat-icon">✉</span>Emails</li>
    <li><span class="cat-icon">⇅</span>Import-kLockTrellis-08.02.23</li>
    <li><span class="cat-icon">⇅</span>Import-kLockTrellis-08.02.23</li>
    <li><span class="cat-icon">⇅</span>Import-kLockTrellis-08.02.23</li>
    <li><span class="cat-icon">▫</span></li>
    <li><span class="cat-icon">▪</span>Test</li>
    <li><span class="cat-icon">▪</span>Test 123</li>
    <li><span class="cat-icon">$</span>Test 1213</li>
    <li><span class="cat-icon">$</span>Test 1213</li>
    <li><span class="cat-icon">▪</span>Test 123x</li>
  </ul>

  <svg width="0" height="0" style="position:absolute">
    <symbol id="folder" viewBox="0 0 14 11"><path fill="#3f73d8" d="M0 1a1 1 0 0 1 1-1h4l1.5 1.5H13a1 1 0 0 1 1 1V10a1 1 0 0 1-1 1H1a1 1 0 0 1-1-1z"/></symbol>
  </svg>

  <div class="grid">
    <div class="entry"><svg width="14" height="11"><use href="#folder"/></svg>Test 333</div>
    <div class="entry"><svg width="14" height="11"><use href="#folder"/></svg>Test 123 1</div>
    <div class="entry"><svg width="14" height="11"><use href="#folder"/></svg>Test 666</div>
    <div class="entry"><svg width="14" height="11"><use href="#folder"/></svg>Marketbay</div>
    <div class="entry"><svg width="14" height="11"><use href="#folder"/></svg>Wikinest</div>
    <div class="entry"><svg width="14" height="11"><use href="#folder"/></svg>Vaultcoin</div>
    <div class="entry"><svg width="14" height="11"><use href="#folder"/></svg>Chirpline</div>
    <div class="entry"><svg width="14" height="11"><use href="#folder"/></svg>jim@harborkeyvault.example</div>
    <div class="entry"><svg width="14" height="11"><use href="#folder"/></svg>Kontaktly</div>
    <div class="entry"><svg width="14" height="11"><use href="#folder"/></svg>Threadly</div>
    <div class="entry"><svg width="14" height="11"><use href="#folder"/></svg>Test ccc</div>
    <div class="entry"><svg width="14" height="11"><use href="#folder"/></svg>Test</div>
    <div class="entry"><svg width="14" height="11"><use href="#folder"/></svg>Filmdex</div>
    <div class="entry"><svg width="14" height="11"><use href="#folder"/></svg>Test 1111</div>
    <div class="entry"><svg width="14" height="11"><use href="#folder"/></svg>Test 77</div>
  </div>
</section>

</body>
</html>
```